Powerpoint visual improvements

I need a cover page, and our beliefs page and differentiating factors page / graphic design for our presentation. For the cover page I would just like an attractive design that incorporate our architectural concept with columns and potentially our logo. For the beliefs page I just want a more attractive presentatoin of the concepts. For the differentiating factors page I want a graphic that captures the points about how we are different from competitors. I have used the attached content to date, but I think it can be improved. The text is included in the graphic and I would also like to make sure the firm logo is incorporated.

Target Market(s)

Individual and institutional investors.

Industry/Entity Type

Investment Advisory

Requirements
Must have
• Our corporate colors are generally RGB 145,148,149; 66,68,76; 0,0,153; and 0,63,127. Our logo is attached. Our primary font is Georgia. Our website is www.PelmarCW.com. The key pages are www.PelmarCW.com/beliefs and www.PelmarCW.com/value we are trying to capture in a presentation. We also need a new presentation cover. Use the website as a reference for the type of imagery we like.

```html
<!DOCTYPE html>
<html lang="en">
<head>
<meta charset="utf-8">
<title>Pelmar Capital Wealth — Presentation Slides</title>
<link rel="stylesheet" href="https://fonts.googleapis.com/css2?family=Arimo:wght@400;700&family=Gelasio:wght@400&display=swap">
<style>
  :root {
    --page-bg: #e0e0e0;
    --slide-border: #cdcdcd;
    --white: #ffffff;
    --header-navy: #3f527a;
    --header-navy-dark: #34497a;
    --label-navy: #1b2b4a;
    --corp-grey: #919495;
    --corp-charcoal: #42444c;
    --corp-blue: #003f7f;
    --sky-top: #9fb5dc;
    --sky-mid: #dfe6f1;
    --sky-low: #c9d6ea;
    --slate: #465d70;
    --amber: #fbbd42;
    --coral: #f06c60;
    --graphite: #636469;
    --teal: #14b09c;
    --azure: #2c96d8;
    --orange: #f39a3a;
    --rose: #ef6a6a;
    --plum: #8a4a8c;
    --deep-blue: #1f67a3;
    --sky-blue: #6ab8e8;
    --mist: #dcdcdc;
    --cycle-logo: #2a6aa3;
    --ink: #111111;
  }
  * { margin: 0; padding: 0; box-sizing: border-box; }
  html, body { width: 1200px; height: 1200px; overflow: hidden; background: var(--page-bg); }
  .canvas { position: relative; width: 1200px; height: 1200px; overflow: hidden; background: var(--page-bg); }
  .slide { position: absolute; left: 264px; width: 655px; background: var(--white); border: 2px solid var(--slide-border); overflow: hidden; }
  .slide svg { display: block; width: 100%; height: 100%; }
  .slide--cover { top: 14px; height: 375px; }
  .slide--beliefs { top: 420px; height: 375px; }
  .slide--value { top: 826px; height: 361px; }
  .sans-label { font-family: "Arimo", Arial, sans-serif; font-weight: 700; }
  .serif-label { font-family: "Gelasio", Georgia, serif; letter-spacing: 1.6px; }
  .brand-name { font-family: "Arimo", Arial, sans-serif; font-weight: 400; }
  .icon-defs { position: absolute; width: 0; height: 0; }
</style>
</head>
<body>
<svg class="icon-defs" aria-hidden="true">
  <defs>
    <symbol id="icon-speaker" viewBox="0 0 24 24">
      <path d="M3 9h4l6-4.5v15L7 15H3z" fill="none" stroke="currentColor" stroke-width="1.6" stroke-linejoin="round"/>
      <path d="M16 9a4 4 0 0 1 0 6M18.5 6.5a7.5 7.5 0 0 1 0 11" fill="none" stroke="currentColor" stroke-width="1.6" stroke-linecap="round"/>
    </symbol>
    <symbol id="icon-search" viewBox="0 0 24 24">
      <circle cx="14" cy="10" r="6.5" fill="none" stroke="currentColor" stroke-width="1.8"/>
      <path d="M9.3 14.7 3 21" stroke="currentColor" stroke-width="2.4" stroke-linecap="round"/>
      <path d="M11.5 12.5l2-2.2 1.6 1.2 2.3-3" fill="none" stroke="currentColor" stroke-width="1.2"/>
    </symbol>
    <symbol id="icon-antenna" viewBox="0 0 24 24">
      <circle cx="12" cy="8.5" r="1.6" fill="currentColor"/>
      <path d="M12 10 8 22M12 10l4 12M9.3 17.5h5.4" fill="none" stroke="currentColor" stroke-width="1.6"/>
      <path d="M8.3 5a5 5 0 0 0 0 7M15.7 5a5 5 0 0 1 0 7M5.5 2.5a9 9 0 0 0 0 12M18.5 2.5a9 9 0 0 1 0 12" fill="none" stroke="currentColor" stroke-width="1.3" stroke-linecap="round"/>
    </symbol>
    <symbol id="icon-case" viewBox="0 0 24 24">
      <rect x="9" y="2" width="6" height="4" rx="1" fill="currentColor"/>
      <path d="M6 8h12l2 14H4z" fill="currentColor"/>
    </symbol>
    <symbol id="icon-puzzle" viewBox="0 0 24 24">
      <rect x="1" y="1" width="11" height="11" fill="#6ab8a0"/>
      <rect x="12" y="1" width="11" height="11" fill="#1b2b4a"/>
      <rect x="1" y="12" width="11" height="11" fill="#7d8c8a"/>
      <rect x="12" y="12" width="11" height="11" fill="#5bb6e8"/>
    </symbol>
  </defs>
</svg>

<main class="canvas">

  <section class="slide slide--cover" aria-label="Cover slide">
    <svg viewBox="0 0 816 467" preserveAspectRatio="none">
      <defs>
        <linearGradient id="cover-header" x1="0" x2="1" y1="0" y2="0">
          <stop offset="0" stop-color="var(--header-navy)"/>
          <stop offset="1" stop-color="var(--header-navy-dark)"/>
        </linearGradient>
        <linearGradient id="cover-sky" x1="0" x2="0" y1="0" y2="1">
          <stop offset="0" stop-color="var(--sky-top)"/>
          <stop offset="0.45" stop-color="var(--sky-mid)"/>
          <stop offset="1" stop-color="var(--sky-low)"/>
        </linearGradient>
      </defs>
      <rect class="cover-header" x="0" y="0" width="816" height="75" fill="url(#cover-header)"/>
      <circle cx="38" cy="40" r="24" fill="var(--white)"/>
      <text class="brand-name" x="68" y="48" font-size="23" fill="var(--white)">Pelmar</text>

      <rect class="cover-scene" x="0" y="75" width="816" height="392" fill="url(#cover-sky)" role="img" aria-label="Six classical white columns of rising height against a blue sky with clouds"/>

      <g class="pillar-labels sans-label" fill="var(--label-navy)" font-size="12.5" text-anchor="middle">
        <use href="#icon-case" x="66" y="224" width="18" height="26" color="var(--label-navy)"/>
        <text x="75" y="266">Experienced</text><text x="75" y="280">Investors</text>

        <use href="#icon-puzzle" x="195" y="160" width="26" height="26"/>
        <text x="208" y="199">Independent</text><text x="208" y="212">Portfolio</text><text x="208" y="226">Construction</text>

        <use href="#icon-speaker" x="337" y="122" width="20" height="20" color="var(--label-navy)"/>
        <text x="347" y="152">Sound</text><text x="347" y="165">Operational</text><text x="347" y="179">Construction</text>

        <use href="#icon-search" x="468" y="158" width="22" height="22" color="var(--label-navy)"/>
        <text x="479" y="194">Proactive Total</text><text x="479" y="208">Fee Management</text>

        <use href="#icon-search" x="602" y="118" width="20" height="20" color="var(--label-navy)"/>
        <text x="612" y="154">Institutional</text><text x="612" y="168">Research Process</text>

        <use href="#icon-antenna" x="739" y="156" width="22" height="24" color="var(--label-navy)"/>
        <text x="750" y="193">Transparent</text><text x="750" y="207">Communication</text>
      </g>
    </svg>
  </section>

  <section class="slide slide--beliefs" aria-label="Beliefs slide">
    <svg viewBox="0 0 818 468" preserveAspectRatio="none">
      <g class="belief-hexagon">
        <polygon points="277,40 393,40 337,143 287,228 226,128" fill="var(--slate)"/>
        <polygon points="393,40 497,40 556,142 437,143 337,143" fill="var(--amber)"/>
        <polygon points="437,143 556,142 605,228 547,330 487,228" fill="var(--coral)"/>
        <polygon points="487,228 547,330 497,418 378,418 437,313" fill="var(--graphite)"/>
        <polygon points="437,313 378,418 277,418 217,315 337,313" fill="var(--teal)"/>
        <polygon points="337,313 217,315 167,228 226,128 287,228" fill="var(--azure)"/>
        <polygon points="287,228 337,143 437,143 487,228 437,313 337,313" fill="var(--white)"/>
      </g>
      <circle cx="387" cy="228" r="72" fill="var(--corp-grey)"/>
      <text class="brand-name" x="387" y="236" font-size="24" fill="var(--white)" text-anchor="middle">Pelmar</text>

      <g class="serif-label" font-size="11.5" fill="var(--white)" text-anchor="middle">
        <use href="#icon-antenna" x="283" y="68" width="22" height="26" color="var(--white)"/>
        <text x="294" y="110">Transparent</text><text x="294" y="122">Communication</text>

        <use href="#icon-case" x="427" y="49" width="26" height="34" color="var(--ink)"/>
        <text x="441" y="102">Experienced</text><text x="441" y="114">Investors</text>

        <use href="#icon-puzzle" x="520" y="166" width="30" height="30"/>
        <text x="540" y="222">Independant</text><text x="540" y="233">Portfolio</text><text x="540" y="245">Construction</text>

        <use href="#icon-search" x="218" y="196" width="34" height="34" color="var(--slate)"/>
        <text x="245" y="248">Institutional</text><text x="245" y="260">Research Process</text>

        <use href="#icon-speaker" x="454" y="296" width="34" height="34" color="var(--ink)"/>
        <text x="469" y="349">Sound</text><text x="469" y="361">Operation</text><text x="469" y="372">Platform</text>

        <use href="#icon-search" x="308" y="334" width="36" height="36" color="var(--corp-blue)"/>
        <text x="325" y="381">Proactive Total</text><text x="325" y="393">Fee Management</text>
      </g>
    </svg>
  </section>

  <section class="slide slide--value" aria-label="Differentiating factors slide">
    <svg viewBox="0 0 818 450" preserveAspectRatio="none">
      <defs>
        <marker id="head-orange" viewBox="0 0 20 20" refX="3" refY="10" markerWidth="46" markerHeight="46" markerUnits="userSpaceOnUse" orient="auto"><path d="M0 0 20 10 0 20z" fill="var(--orange)"/></marker>
        <marker id="head-rose" viewBox="0 0 20 20" refX="3" refY="10" markerWidth="46" markerHeight="46" markerUnits="userSpaceOnUse" orient="auto"><path d="M0 0 20 10 0 20z" fill="var(--rose)"/></marker>
        <marker id="head-plum" viewBox="0 0 20 20" refX="3" refY="10" markerWidth="46" markerHeight="46" markerUnits="userSpaceOnUse" orient="auto"><path d="M0 0 20 10 0 20z" fill="var(--plum)"/></marker>
        <marker id="head-deep" viewBox="0 0 20 20" refX="3" refY="10" markerWidth="46" markerHeight="46" markerUnits="userSpaceOnUse" orient="auto"><path d="M0 0 20 10 0 20z" fill="var(--deep-blue)"/></marker>
        <marker id="head-sky" viewBox="0 0 20 20" refX="3" refY="10" markerWidth="46" markerHeight="46" markerUnits="userSpaceOnUse" orient="auto"><path d="M0 0 20 10 0 20z" fill="var(--sky-blue)"/></marker>
        <marker id="head-mist" viewBox="0 0 20 20" refX="3" refY="10" markerWidth="46" markerHeight="46" markerUnits="userSpaceOnUse" orient="auto"><path d="M0 0 20 10 0 20z" fill="var(--mist)"/></marker>
      </defs>

      <g class="cycle-arrows" fill="none" stroke-width="26">
        <path d="M446 77 A152 152 0 0 1 490 100" stroke="var(--orange)" marker-end="url(#head-orange)"/>
        <path d="M548 192 A152 152 0 0 1 549 240" stroke="var(--rose)" marker-end="url(#head-rose)"/>
        <path d="M500 335 A152 152 0 0 1 460 362" stroke="var(--plum)" marker-end="url(#head-plum)"/>
        <path d="M350 366 A152 152 0 0 1 306 342" stroke="var(--deep-blue)" marker-end="url(#head-deep)"/>
        <path d="M247 252 A152 152 0 0 1 247 204" stroke="var(--sky-blue)" marker-end="url(#head-sky)"/>
        <path d="M296 109 A152 152 0 0 1 336 84" stroke="var(--mist)" marker-end="url(#head-mist)"/>
      </g>

      <g class="cycle-nodes">
        <circle cx="398" cy="70" r="44" fill="var(--white)" stroke="var(--orange)" stroke-width="6"/>
        <circle cx="530" cy="146" r="44" fill="var(--white)" stroke="var(--rose)" stroke-width="6"/>
        <circle cx="530" cy="298" r="44" fill="var(--white)" stroke="var(--plum)" stroke-width="6"/>
        <circle cx="398" cy="374" r="44" fill="var(--white)" stroke="var(--deep-blue)" stroke-width="6"/>
        <circle cx="266" cy="298" r="44" fill="var(--white)" stroke="var(--sky-blue)" stroke-width="6"/>
        <circle cx="266" cy="146" r="44" fill="var(--white)" stroke="var(--mist)" stroke-width="6"/>
      </g>

      <circle cx="398" cy="222" r="48" fill="var(--cycle-logo)"/>
      <text class="brand-name" x="398" y="229" font-size="19" fill="var(--white)" text-anchor="middle">Pelmar</text>

      <g class="sans-label" font-size="10.5" fill="var(--ink)" text-anchor="middle">
        <use href="#icon-case" x="390" y="46" width="16" height="22" color="var(--ink)"/>
        <text x="398" y="82">Experienced</text><text x="398" y="93">Investors</text>

        <use href="#icon-puzzle" x="522" y="120" width="18" height="18"/>
        <text x="532" y="151">Independant</text><text x="532" y="162">Portfolio</text><text x="532" y="173">Construction</text>

        <use href="#icon-speaker" x="525" y="271" width="20" height="20" color="var(--ink)"/>
        <text x="535" y="303">Sound</text><text x="535" y="314">Operation</text><text x="535" y="325">Platform</text>

        <use href="#icon-search" x="386" y="340" width="22" height="22" color="var(--deep-blue)"/>
        <text x="396" y="374">Proactive</text><text x="397" y="385">Total Fee</text><text x="398" y="396">Management</text>

        <use href="#icon-search" x="254" y="273" width="20" height="20" color="var(--corp-grey)"/>
        <text x="264" y="304">Institutional</text><text x="263" y="315">Research</text><text x="264" y="326">Process</text>

        <use href="#icon-antenna" x="250" y="118" width="22" height="24" color="var(--ink)"/>
        <text x="261" y="154">Transparent</text><text x="261" y="165">Communication</text>
      </g>
    </svg>
  </section>

</main>
</body>
</html>
```